Wordpress Design for Fruit & Veggie Swap Site

I need a wordpress design for the HOME PAGE of a company located in Kona, Hawaii called Leaf Loop Hawaii. Leaf Loop Hawaii (LLH) is a site intended to support the local food movement by connecting neighbors in order for them to swap/trade produce from their farm or garden. The purpose of this site is to support sustainable agriculture in Hawaii and encourage community interaction.

The model of the site is similar to:
http://www.harvtrade.me/ (I really like the simple design of this site)
http://www.plotbarter.co.uk/ (I don't like the design of this site, just the functionality. The design is too busy and unbalanced.)
Unlike the two sites listed above, however, LLH is only targeted at people living on the Big Island of Hawaii.

The site is simply intended to be a platform to connect people, then they are free to swap or barter off site, similar to the way tradeboard connects people. Users can create "posts" for crops that they have available for swap, which are searchable based on name and location.

I have created a very basic, no-css, dev version of the site to work on the back end, which is located here: http://leafloophawaii.com/test
Feel free to register and create a test post to get a feel for how it works.

The images I have uploaded are just for ideas and do not have to be in the design.
Updates

Reason: I extended the deadline so you have more time to work on designs. Thank you!

Target Market(s)

The targeted audience is gardeners and farmers on the Big Island of Hawaii. These people are quite varied in age and technical ability.

Industry/Entity Type

Agriculture

Requirements
Must have
• On the homepage, I would like to have a list of the most recent "posts", displayed as the post title, with the most recent post at the top of the list. In the test site, this is located in the right column, but it doesn't have to be in that location in the final design.

I would also like the option to "Add new listing" to be displayed creatively on the home page. This can be in the form of a graphic that links to a form on another page.

I would also like to have a search box on the homepage. Users can search by crop name and/or location.

The main focal point of the home page will be a map area fill map application of the Big Island. I am in the process of developing this. You can see the map on the test site, please keep in mind that this map may change slightly in future revisions. Feel free to change the size and styling of the map to fit your design.

I would like the homepage to have a simple and clean layout, making it clear to users how the site works.
For the graphics, I would like to incorporate the "crop circles" idea (yes, like the alien crop circles in fields) with fruits and veggies (including tropical fruit found in Hawaii like banana, coconut, lychee, taro, oranges, as well as traditional vegetables like carrots, lettuce, etc.), and also potentially with the idea of sharing and circulating produce with neighbors.
Please note that those specific fruits and veggies don't need to be used, or that many of them, I was just giving them as examples.

I would also like to have a place on the homepage where users can login/sign up. This can be a login form with a sign up link, or a login link and a sign up link.

I would like the entire design to fit on a page without having to scroll.

Once the site has a substantial user base, I plan to incorporate advertising. Please create a design that will be easy to integrate ads into in the future, most likely in the side bar or footer. I do not want the original design to have ad space, just the ability to add it easily in the future and having it look good with the current design.

```html
<!DOCTYPE html>
<html lang="en">
<head>
<meta charset="utf-8">
<title>Leaf Loop Hawaii</title>
<link rel="stylesheet" href="https://fonts.googleapis.com/css2?family=Shadows+Into+Light+Two&family=Arimo:wght@700&display=swap">
<style>
  :root {
    --meadow-light: #eef3e6;
    --meadow-mid: #cfe2c4;
    --meadow-deep: #9cc49a;
    --panel: #c99460;
    --panel-edge: #b88350;
    --bark: #6b3a0f;
    --bark-soft: #8a5428;
    --ink: #5a3210;
    --cream: #ffffff;
    --map-sea: #a8c2dc;
    --map-land: #cfd8c4;
    --produce-green: #8cc152;
    --produce-yellow: #f1cd3c;
    --produce-red: #d9261f;
  }
  * { box-sizing: border-box; margin: 0; padding: 0; }
  html, body { width: 1200px; height: 747px; overflow: hidden; }
  body { font-family: "Shadows Into Light Two", cursive; color: var(--ink); }

  .page {
    position: relative; width: 1200px; height: 747px; overflow: hidden;
    background: radial-gradient(ellipse at 50% 40%, var(--meadow-light) 0%, var(--meadow-mid) 60%, var(--meadow-deep) 100%);
  }
  .meadow { position: absolute; inset: 0; }

  .brand {
    position: absolute; left: 0; width: 1200px; top: 44px; text-align: center;
    font-size: 58px; line-height: 1; color: var(--bark-soft);
  }

  .board {
    position: absolute; left: 189px; top: 145px; width: 870px; height: 584px;
    background: var(--panel); border-radius: 22px 14px 26px 18px;
    box-shadow: 0 0 0 3px var(--panel-edge), 0 2px 10px rgba(80,50,20,.25);
  }

  .produce {
    position: absolute; left: 126px; top: 112px; width: 168px; height: 128px;
    border-radius: 40%;
    background: radial-gradient(ellipse at 45% 45%, var(--produce-yellow) 0%, var(--produce-green) 55%, rgba(217,38,31,.85) 100%);
  }

  .nav { position: absolute; top: 176px; left: 0; width: 1200px; height: 30px; font-size: 21px; line-height: 30px; }
  .nav a { position: absolute; color: var(--ink); text-decoration: none; white-space: nowrap; }
  .nav .home { left: 408px; }
  .nav .about { left: 502px; }
  .nav .blog { left: 661px; }
  .nav .contact { left: 755px; }
  .nav .login { left: 971px; top: -22px; }
  .nav-marker {
    position: absolute; left: 424px; top: 158px; width: 20px; height: 20px;
    border-radius: 50%; background: radial-gradient(circle at 40% 40%, #ef4a3f, var(--produce-red));
  }

  .section-title {
    position: absolute; font-size: 36px; line-height: 44px; color: var(--cream); text-align: center;
    text-shadow: 0 1px 4px rgba(60,30,5,.45); white-space: nowrap; font-weight: 400;
  }
  .title-posts { left: 216px; width: 213px; top: 232px; }
  .title-search { left: 480px; width: 305px; top: 226px; }
  .title-signup { left: 831px; width: 202px; top: 234px; }

  .recent-posts {
    position: absolute; left: 216px; top: 279px; width: 213px; height: 350px;
    background: var(--bark-soft); border-radius: 16px; list-style: none;
    padding: 10px 38px 0; text-align: center;
    font-family: "Arimo", Arial, sans-serif; font-weight: 700; font-size: 12.3px;
    line-height: 14.8px; color: var(--cream);
  }

  .field {
    position: absolute; height: 29px; border-radius: 15px; background: var(--bark);
    color: var(--cream); padding-left: 16px; line-height: 29px; font-size: 16px; white-space: nowrap;
  }
  .field-search { left: 480px; top: 279px; width: 234px; font-family: "Arimo", Arial, sans-serif; font-weight: 700; font-size: 13px; }
  .field-name { left: 831px; top: 305px; width: 202px; }
  .field-email { left: 831px; top: 345px; width: 202px; }

  .button {
    position: absolute; height: 29px; border-radius: 15px; background: var(--bark);
    color: var(--cream); text-align: center; line-height: 29px; font-size: 16px;
  }
  .button-search { left: 723px; top: 279px; width: 62px; }
  .button-go { left: 970px; top: 385px; width: 61px; }

  .map {
    position: absolute; left: 482px; top: 325px; width: 306px; height: 257px;
    border: 4px solid #8d7d6c; border-radius: 3px;
    background: linear-gradient(160deg, var(--map-sea) 0%, var(--map-land) 100%);
    box-shadow: 0 0 4px rgba(0,0,0,.3);
  }

  .add-post {
    position: absolute; left: 849px; top: 474px; font-size: 25px; line-height: 36px; color: var(--ink);
    text-decoration: none; white-space: nowrap;
  }
  .add-post .plus { font-size: 34px; vertical-align: -3px; margin-right: 6px; }

  .copyright { position: absolute; left: 288px; top: 661px; font-size: 12px; line-height: 16px; }

  .social { position: absolute; left: 949px; top: 662px; display: flex; gap: 5px; }
  .social span { width: 19px; height: 19px; background: var(--bark); border-radius: 2px; display: block; }
</style>
</head>
<body>
<div class="page">
  <div class="meadow" role="img" aria-label="Grassy meadow surrounding the page"></div>

  <div class="brand">leafloop</div>

  <div class="board"></div>
  <div class="produce" role="img" aria-label="Illustration of fresh vegetables"></div>

  <nav class="nav">
    <a class="home" href="#">Home</a>
    <a class="about" href="#">About Us</a>
    <a class="blog" href="#">Blog</a>
    <a class="contact" href="#">Contact Us</a>
    <a class="login" href="#">Login</a>
  </nav>
  <div class="nav-marker" role="img" aria-label="Small produce icon marking the current page"></div>

  <h2 class="section-title title-posts">Recent Posts</h2>
  <ul class="recent-posts">
    <li>Lemons (Pahala)</li>
    <li>Oranges (Kohala)</li>
    <li>Coconuts (hilo)</li>
    <li>Lettuce (Holualoa)</li>
    <li>Testuser trying to add photo (Hawi)</li>
    <li>New post from testuser with map and photo (honokaa)</li>
    <li>New post from testuser (honokaa)</li>
    <li>Papaya seedlings (captain cook)</li>
    <li>2 Dozen Organic Eggs (Kealakekua)</li>
    <li>Coffee cherries (kapoho)</li>
    <li>Bamboo plants (Captain Cook)</li>
    <li>Kona limes (pahoa)</li>
    <li>Mango (pahoa)</li>
    <li>Taro root (pahoa)</li>
    <li>Pineapple (Naalehu)</li>
  </ul>

  <h2 class="section-title title-search">Search</h2>
  <div class="field field-search">Search for</div>
  <div class="button button-search">Search</div>
  <div class="map" role="img" aria-label="Interactive map of the Big Island showing crop post locations"></div>

  <h2 class="section-title title-signup">Sign Up</h2>
  <div class="field field-name">Name</div>
  <div class="field field-email">Email</div>
  <div class="button button-go">Go</div>

  <a class="add-post" href="#"><span class="plus">+</span>Add New Post</a>

  <div class="copyright">Copyright 2013</div>
  <div class="social"><span></span><span></span><span></span><span></span></div>
</div>
</body>
</html>
```